The Perfect Business Card for PineHarbor

I am looking for a business card which beautifully incorporates my logo, reflects my business and looks special, elegant and clean.

```html
<!DOCTYPE html>
<html lang="en">
<head>
<meta charset="utf-8">
<title>PineHarbor – Business Card</title>
<link href="https://fonts.googleapis.com/css2?family=Montserrat:wght@400;700&display=swap" rel="stylesheet">
<style>
  :root {
    --bg: #d9d9d9;
    --paper: #ffffff;
    --green: #6a8f33;
    --green-light: #7aa33a;
    --green-dark: #587a2c;
    --ink-green: #4e6e25;
  }
  * { box-sizing: border-box; margin: 0; padding: 0; }
  html, body { width: 1200px; height: 846px; overflow: hidden; }
  body {
    background: var(--bg);
    font-family: "Montserrat", sans-serif;
    display: flex;
    align-items: center;
    justify-content: center;
    gap: 60px;
  }
  .card {
    position: relative;
    width: 510px;
    height: 320px;
    overflow: hidden;
    box-shadow: 0 12px 30px rgba(0,0,0,0.18);
  }
  /* Front side */
  .card--front { background: var(--paper); }
  .front__arc {
    position: absolute;
    width: 420px;
    height: 420px;
    right: -150px;
    top: -210px;
    border-radius: 50%;
    background: radial-gradient(circle at 40% 65%, var(--green-light), var(--green-dark) 75%);
  }
  .brand {
    display: flex;
    align-items: center;
    gap: 10px;
    color: var(--green);
    font-weight: 400;
    font-size: 30px;
    letter-spacing: 1px;
  }
  .brand__dot {
    width: 30px; height: 30px;
    border: 2px solid currentColor;
    border-radius: 50%;
  }
  .front__brand { position: absolute; left: 34px; top: 130px; }
  .contact {
    position: absolute;
    left: 215px;
    top: 190px;
    color: var(--ink-green);
  }
  .contact__name { font-weight: 700; font-size: 15px; margin-bottom: 10px; }
  .contact__row {
    display: flex; align-items: center; gap: 8px;
    font-size: 12px; line-height: 1.3; margin-bottom: 5px;
  }
  .contact__row svg { width: 13px; height: 13px; flex: none; fill: var(--ink-green); }
  /* Back side */
  .card--back {
    background: radial-gradient(ellipse at 50% 45%, var(--green-light), var(--green-dark) 85%);
    display: flex;
    align-items: center;
    justify-content: center;
  }
  .card--back .brand { color: var(--paper); font-size: 44px; gap: 16px; }
  .card--back .brand__dot { width: 44px; height: 44px; }
</style>
</head>
<body>
  <section class="card card--front">
    <div class="front__arc"></div>
    <div class="brand front__brand"><span class="brand__dot"></span>PineHarbor</div>
    <div class="contact">
      <p class="contact__name">Mara Lindqvist</p>
      <p class="contact__row">
        <svg viewBox="0 0 24 24"><path d="M6.6 10.8a15 15 0 0 0 6.6 6.6l2.2-2.2a1 1 0 0 1 1-.25 11.4 11.4 0 0 0 3.6.57 1 1 0 0 1 1 1V20a1 1 0 0 1-1 1A17 17 0 0 1 3 4a1 1 0 0 1 1-1h3.5a1 1 0 0 1 1 1c0 1.25.2 2.45.57 3.57a1 1 0 0 1-.25 1z"/></svg>
        +41 (0)76 482 05 36
      </p>
      <p class="contact__row">
        <svg viewBox="0 0 24 24"><path d="M2 6h20v12H2zm2 2v.5l8 5 8-5V8l-8 5z"/></svg>
        info@pineharbor.ch
      </p>
      <p class="contact__row">
        <svg viewBox="0 0 24 24"><path d="M12 2a7 7 0 0 0-7 7c0 5 7 13 7 13s7-8 7-13a7 7 0 0 0-7-7zm0 9.5A2.5 2.5 0 1 1 12 6.5a2.5 2.5 0 0 1 0 5z"/></svg>
        <span>Birkenweg 7<br>8004 Zürich</span>
      </p>
    </div>
  </section>

  <section class="card card--back">
    <div class="brand"><span class="brand__dot"></span>PineHarbor</div>
  </section>
</body>
</html>
```